Health Coaching Brochure for Healthcare Practioners

I am looking to have a tri-fold brochure created marketed towards healthcare practitioners (doctors, nurses, surgeons, etc), to get them to purchase 1-on-1 health coaching from me.
I've provided the text/content (in pdf & pages), my logo, a picture of me, and two color palettes, but please also include lots of white space. I would like to design to be very clean, modern & crisp. Also include additional photos, of doctors, etc taking care of themselves & feeling happy (maybe eating healthy, maybe exercising, feeling good & happy!)
Please also see http://brightoakwellness.com and http://instagram.com/brightoakwellness for a feel of my brand.
Thank you!
Target Market(s)
Healthcare Practioners (mainly based in Los Angeles, for now)
Industry/Entity Type
Healthcare
Look and feel

```html
<!DOCTYPE html>
<html lang="en">
<head>
<meta charset="utf-8">
<title>Bright Oak Wellness – Tri-fold Brochure</title>
<link href="https://fonts.googleapis.com/css2?family=Source+Sans+3:wght@300;400;600;700&family=Montserrat:wght@400;500&family=Dancing+Script:wght@500&display=swap" rel="stylesheet">
<style>
:root{
  --teal:#3fbfc2;
  --teal-dark:#2fa9ac;
  --green:#8dc63f;
  --green-light:#c9e08f;
  --ink:#4a4a4a;
  --muted:#6b6b6b;
  --paper:#ffffff;
  --backdrop:#d6d7d8;
}
*{box-sizing:border-box;margin:0;padding:0}
html,body{width:877px;height:1200px;overflow:hidden;background:var(--backdrop)}
body{font-family:"Source Sans 3",Arial,sans-serif;color:var(--ink);position:relative}
.sheet{position:absolute;left:121px;width:648px;height:504px;display:flex;background:var(--paper);box-shadow:0 10px 14px -6px rgba(0,0,0,.35)}
.sheet--outside{top:67px}
.sheet--inside{top:622px}
.panel{position:relative;width:216px;height:100%;overflow:hidden}
.panel--teal{background:var(--teal);color:#fff}
.panel--white{background:linear-gradient(90deg,#f1f2f2,#fff 12%,#fff 88%,#f1f2f2)}
.photo{position:absolute}
.abs{position:absolute}
h3.label{font-weight:700;font-size:9px;letter-spacing:.1px;text-transform:uppercase;line-height:1.25}
.body-copy{font-size:8.4px;line-height:1.25;font-weight:400}
.bullets{list-style:none;font-size:8.6px;line-height:1.6}
.bullets li{position:relative;padding-left:10px}
.bullets li::before{content:"";position:absolute;left:0;top:4px;width:6px;height:6px;border-radius:50%;background:#fff}
.bullets--qa{color:var(--muted);font-size:8.2px;line-height:1.2}
.bullets--qa li{padding-left:13px;margin-bottom:8px}
.bullets--qa li::before{background:var(--teal);top:3px}
.brand{font-family:"Source Sans 3",sans-serif;font-weight:700;font-size:17px;letter-spacing:.3px}
.brand--ink{color:var(--ink)}
.brand--white{color:#fff}
.green-head{color:var(--green);font-weight:700;font-size:9.4px;text-align:center;line-height:1.25}
.teal-head{color:var(--teal);font-weight:600;font-size:9.6px;text-align:center;line-height:1.25}
.phone-pill{position:absolute;left:33px;width:150px;height:22px;border-radius:11px;background:var(--green);color:#fff;font-weight:600;font-size:14px;display:flex;align-items:center;justify-content:center;gap:4px}
.center-copy{text-align:center;font-size:10.4px;line-height:1.25;color:var(--ink)}
.display{font-family:"Montserrat",sans-serif;font-weight:400;letter-spacing:2px;font-size:14px;line-height:1.1}
.ticks{list-style:none;font-size:8.6px;line-height:1.4;color:var(--ink)}
.ticks li{display:flex;align-items:center;gap:6px}
.script{font-family:"Dancing Script",cursive;color:#fff;font-size:9.2px;line-height:1.3}
.quote{display:flex;gap:5px;font-size:8.2px;line-height:1.22}
.quote .mark{color:var(--green-light);font-family:Georgia,serif;font-size:18px;line-height:.8;font-weight:700}
</style>
</head>
<body>

<!-- Outside of the brochure -->
<section class="sheet sheet--outside">

  <!-- About panel -->
  <article class="panel panel--teal">
    <h3 class="label abs" style="left:13px;top:52px">About Bright Oak Wellness</h3>
    <p class="body-copy abs" style="left:13px;top:72px;width:192px;text-align:justify">Amelia Cordero is holistic health coach, personal trainer, and fitness nutritionist who empowers healthcare practitioners who are exhausted and overwhelmed to find uncomplicated ways to minimize their stress and to make themselves and their health a priority.</p>
    <h3 class="label abs" style="left:13px;top:176px">Services include:</h3>
    <ul class="bullets abs" style="left:13px;top:192px">
      <li>1-on-1 Virtuel Health Coaching</li>
      <li>1-on-1 Personal Training</li>
      <li>Virtuel Group Coaching</li>
      <li>Custom Workout Program and/or Meal Plan</li>
      <li>Grocery Store Tour</li>
      <li>Pantry Clean Out</li>
    </ul>
    <svg class="photo" style="left:0;top:305px" width="216" height="199" viewBox="0 0 216 199" role="img" aria-label="Portrait photo of the health coach smiling">
      <defs><linearGradient id="portrait" x1="0" y1="0" x2="1" y2="1"><stop offset="0" stop-color="#cfcac5"/><stop offset=".55" stop-color="#8a6d5e"/><stop offset="1" stop-color="#3a2a24"/></linearGradient></defs>
      <path d="M0 20 Q110 -12 216 24 V199 H0Z" fill="url(#portrait)"/>
      <path d="M0 20 Q110 -12 216 24" fill="none" stroke="var(--green-light)" stroke-width="4"/>
    </svg>
  </article>

  <!-- Back cover panel -->
  <article class="panel panel--white">
    <svg class="photo" style="left:4px;top:0" width="208" height="185" viewBox="0 0 208 185" role="img" aria-label="Photo of colourful roasted vegetables">
      <defs><radialGradient id="veg"><stop offset="0" stop-color="#e0673a"/><stop offset=".6" stop-color="#7a9a3a"/><stop offset="1" stop-color="#b9925f"/></radialGradient></defs>
      <circle cx="112" cy="40" r="102" fill="url(#veg)"/>
      <circle cx="68" cy="130" r="54" fill="var(--teal)"/>
    </svg>
    <p class="script abs" style="left:22px;top:104px;width:100px">Together we can reclaim your health and create a life more joyful than you ever imagined!</p>
    <div class="brand brand--ink abs" style="left:0;width:216px;text-align:center;top:212px">Bright Oak Wellness</div>
    <p class="green-head abs" style="left:0;width:216px;top:252px">GLENDALE LOCATION OR<br>AT-HOME WORKOUTS</p>
    <p class="abs" style="left:0;width:216px;top:290px;text-align:center;font-size:8.6px;font-weight:600">call for a free 15 minute consultation</p>
    <div class="phone-pill" style="top:310px">
      <svg width="13" height="13" viewBox="0 0 14 14"><circle cx="7" cy="7" r="6" fill="none" stroke="#fff" stroke-width="1.3"/><path d="M4.6 4.2c.4-.4.9-.3 1.1.1l.5.9c.2.4 0 .7-.3.9.3.7.9 1.3 1.6 1.6.2-.3.5-.5.9-.3l.9.5c.4.2.5.7.1 1.1-.9.9-2.4.4-3.7-.9S3.7 5.1 4.6 4.2z" fill="#fff"/></svg>
      718.555.0142
    </div>
    <p class="center-copy abs" style="left:0;width:216px;top:342px">1-ON-1 PERSONAL TRAINING,<br>LOS ANGELES, CA</p>
    <svg class="photo" style="left:50px;top:395px" width="166" height="109" viewBox="0 0 166 109" role="img" aria-label="Photo of a green smoothie in a glass">
      <defs><linearGradient id="smoothie" x1="0" y1="0" x2="1" y2="1"><stop offset="0" stop-color="#2f5a22"/><stop offset=".5" stop-color="#6fa83a"/><stop offset="1" stop-color="#aacb6a"/></linearGradient></defs>
      <path d="M10 109 Q0 60 30 55 L40 109Z" fill="var(--green-light)"/>
      <circle cx="80" cy="80" r="75" fill="url(#smoothie)"/>
    </svg>
  </article>

  <!-- Front cover panel -->
  <article class="panel panel--teal">
    <svg class="photo" style="left:0;top:0" width="216" height="295" viewBox="0 0 216 295" role="img" aria-label="Photo of a woman jogging outdoors in workout clothes">
      <defs><linearGradient id="runner" x1="0" y1="0" x2="1" y2="1"><stop offset="0" stop-color="#8d7d74"/><stop offset=".5" stop-color="#b8aaa0"/><stop offset="1" stop-color="#6d6a63"/></linearGradient></defs>
      <rect width="216" height="295" fill="url(#runner)"/>
      <path d="M0 220 Q110 270 216 245 V295 H0Z" fill="var(--teal)"/>
      <path d="M0 212 Q110 262 216 238" fill="none" stroke="var(--green)" stroke-width="4"/>
    </svg>
    <div class="brand brand--white abs" style="left:0;width:216px;text-align:center;top:302px">Bright Oak Wellness</div>
    <p class="center-copy abs" style="left:0;width:216px;top:333px;color:#fff">1-ON-1 PERSONAL TRAINING,<br>LOS ANGELES, CA</p>
    <svg class="abs" style="left:0;top:370px" width="216" height="134" viewBox="0 0 216 134">
      <path d="M0 20 Q120 -10 216 50 V134 H0Z" fill="#fff"/>
      <path d="M0 14 Q120 -16 216 48" fill="none" stroke="var(--green-light)" stroke-width="5"/>
    </svg>
    <h2 class="display abs" style="left:36px;top:408px;color:var(--teal);text-align:center;width:170px">CHANGE<br>THE WAY YOU LIVE</h2>
    <ul class="ticks abs" style="left:41px;top:445px">
      <li><svg width="7" height="7" viewBox="0 0 8 8"><circle cx="4" cy="4" r="3.4" fill="none" stroke="var(--teal)"/><path d="M2.4 4l1 1 2-2" stroke="var(--teal)" fill="none"/></svg>GET IN SHAPE</li>
      <li><svg width="7" height="7" viewBox="0 0 8 8"><circle cx="4" cy="4" r="3.4" fill="none" stroke="var(--teal)"/><path d="M2.4 4l1 1 2-2" stroke="var(--teal)" fill="none"/></svg>LOSE WEIGHT</li>
      <li><svg width="7" height="7" viewBox="0 0 8 8"><circle cx="4" cy="4" r="3.4" fill="none" stroke="var(--teal)"/><path d="M2.4 4l1 1 2-2" stroke="var(--teal)" fill="none"/></svg>TONE UP</li>
      <li><svg width="7" height="7" viewBox="0 0 8 8"><circle cx="4" cy="4" r="3.4" fill="none" stroke="var(--teal)"/><path d="M2.4 4l1 1 2-2" stroke="var(--teal)" fill="none"/></svg>LOOK &amp; FEEL BETTER THAN EVER</li>
    </ul>
  </article>
</section>

<!-- Inside of the brochure -->
<section class="sheet sheet--inside">

  <!-- Training panel -->
  <article class="panel panel--teal">
    <svg class="photo" style="left:0;top:0" width="216" height="210" viewBox="0 0 216 210" role="img" aria-label="Photo of a woman doing push-ups with bananas and a protein shake">
      <defs><linearGradient id="pushup" x1="0" y1="0" x2="1" y2="1"><stop offset="0" stop-color="#fbfbfb"/><stop offset=".6" stop-color="#e9e2dc"/><stop offset="1" stop-color="#c9b07a"/></linearGradient></defs>
      <path d="M0 0 H216 V190 Q110 205 0 170Z" fill="url(#pushup)"/>
      <path d="M0 170 Q110 205 216 190" fill="none" stroke="var(--green-light)" stroke-width="6"/>
      <circle cx="170" cy="176" r="38" fill="#e6d38a" stroke="var(--green-light)" stroke-width="3"/>
    </svg>
    <h3 class="label abs" style="left:13px;top:209px;width:195px">Get the most out of<br>your workout by working out<br>with a personl trainer</h3>
    <ul class="bullets abs" style="left:13px;top:254px">
      <li>Customized workout program,</li>
      <li>from beginnier to advanced</li>
      <li>Provide motivation, support, and accountability</li>
      <li>Integrative Nutrition &amp; Health Coaching</li>
      <li>+24-hour access to trainer</li>
    </ul>
    <h3 class="label abs" style="left:13px;top:340px">Achieve your fitness goals<br>and have fun doing it</h3>
    <ul class="bullets abs" style="left:13px;top:365px">
      <li>Fat Loss</li>
      <li>Weight Training</li>
      <li>Cardiovascular Training</li>
      <li>Muscular Development &amp; Toning</li>
      <li>Sports Performance Training</li>
      <li>Body Composition Analysis</li>
      <li>Specialized Diet Plans</li>
      <li>Nutrition &amp; Supplementation Counseling</li>
      <li>Wedding Preparation</li>
    </ul>
  </article>

  <!-- Questions panel -->
  <article class="panel panel--white">
    <svg class="abs" style="left:0;top:0" width="216" height="160" viewBox="0 0 216 160">
      <path d="M18 0 H192 Q200 60 140 72 Q80 80 40 60 Q14 42 18 0Z" fill="var(--green)"/>
      <circle cx="127" cy="105" r="50" fill="var(--teal)"/>
    </svg>
    <p class="abs" style="left:28px;width:160px;top:16px;text-align:center;color:#fff;font-size:8.8px;line-height:1.5"><b>FUNCTION MOVEMENTS!</b><br>based on how your body was<br>designed to move</p>
    <p class="abs" style="left:82px;width:90px;top:88px;text-align:center;color:#fff;font-weight:700;font-size:9.2px;line-height:1.3">It's time to take care of YOU.<br>You deserve it!</p>
    <p class="teal-head abs" style="left:8px;width:200px;top:178px">Are you overwhelmed and exhausted and feel like there's no time left for YOU?</p>
    <ul class="bullets bullets--qa abs" style="left:10px;top:212px;width:200px">
      <li>Do you put everyone and everything else before your own health?</li>
      <li>Are you struggling with how to fit in exercise after working 12-15 hours shifts?</li>
      <li>Do you know exactly what you should do take care of yourself, but it's just not happening?</li>
      <li>Have you gained weight due to stress-eating, and ready to take it off?</li>
      <li>Are you ready to feel energetic and sexy and to fully love yourself again?</li>
    </ul>
    <p class="teal-head abs" style="left:0;width:216px;top:378px;font-size:9px"><span style="color:var(--green)">READY TO MAKE THE COMMITMENT?</span><br>schedule your 15 minute consultation today!</p>
    <div class="phone-pill" style="top:409px">
      <svg width="13" height="13" viewBox="0 0 14 14"><circle cx="7" cy="7" r="6" fill="none" stroke="#fff" stroke-width="1.3"/><path d="M4.6 4.2c.4-.4.9-.3 1.1.1l.5.9c.2.4 0 .7-.3.9.3.7.9 1.3 1.6 1.6.2-.3.5-.5.9-.3l.9.5c.4.2.5.7.1 1.1-.9.9-2.4.4-3.7-.9S3.7 5.1 4.6 4.2z" fill="#fff"/></svg>
      718.555.0142
    </div>
    <p class="abs" style="left:7px;width:203px;top:452px;font-size:8.4px;line-height:1.2;color:var(--muted);text-align:justify">As healthcare practitioners, it's easy to lose sight of your own wants and needs, when you're so busy taking care of everyone else.</p>
  </article>

  <!-- Testimonials panel -->
  <article class="panel panel--teal">
    <h2 class="display abs" style="left:0;width:216px;top:22px;color:#fff;text-align:center">CHANGE<br>THE WAY YOU LIVE</h2>
    <p class="abs" style="left:12px;width:193px;top:64px;font-size:7.4px;line-height:1.2;text-align:justify">Helping others is my passion. Seeing the change in someone throughout their fitness journey is incredible. Not just physically, but also emotionally. They have become more confident, more optimistic, healthier and stronger in all aspects of their life.</p>
    <p class="abs" style="left:12px;width:193px;top:122px;font-size:7.4px;line-height:1.2;text-align:justify">Working with all different skill sets and fitness levels I am always working for my clients. Doing everything I can to teach them how to live a healthier life.</p>
    <div class="quote abs" style="left:12px;width:195px;top:180px">
      <span class="mark">“</span>
      <div><p>I am so happy with the results!</p><p style="margin-top:10px;text-align:justify">The fogginess is gone (as are my sugar cravings). I've found new ways to add healthy foods into my diet and (bonus) I lost five pounds the first week!</p><p style="margin-top:10px">Jenna Fields</p></div>
    </div>
    <div class="quote abs" style="left:12px;width:195px;top:275px">
      <span class="mark">“</span>
      <div><p style="text-align:justify">She's helped me transform myself from an overweight junk food eater to a much fitter and healthier person.</p><p style="margin-top:10px;text-align:justify">I highly recommend Amelia to anyone and everyone.</p><p style="margin-top:10px">Laura Bennett</p></div>
    </div>
    <svg class="photo" style="left:0;top:375px" width="216" height="129" viewBox="0 0 216 129" role="img" aria-label="Photo of a doctor with a stethoscope beside fresh fruit">
      <defs><linearGradient id="doctor" x1="0" y1="0" x2="1" y2="1"><stop offset="0" stop-color="#eef1f3"/><stop offset=".55" stop-color="#d9dee2"/><stop offset="1" stop-color="#f09a3a"/></linearGradient></defs>
      <path d="M0 30 Q100 0 216 12 V129 H0Z" fill="url(#doctor)"/>
      <path d="M0 30 Q100 0 216 12" fill="none" stroke="var(--green-light)" stroke-width="4"/>
    </svg>
  </article>
</section>

</body>
</html>
```